Visitenkarte für Selbständigen
Zielgruppe
Ich bin Selbständiger Unternehmer, der sowohl Versicherungs/Finanzprodukte vertreibt, sowie Immobilien zur Kapitalanlage.
Aufgabenstellung
Ich hätte gern eine zweiseitige Karte. Vorderseite Name und meine Initialen als Logo.
Rückseite Name, Anschrift und telnr.
Berufsbezeichnung muss nicht zwingend mit auf der Karte sein.
Die Karte sollte schwarz oder weiß sein und auf der Vorderseite Name und Logo in Silber (Spiegel Folie)
Timo Harlang
Lindenweg 17
67382 Wiesenau
email: info@timo-harlang.de
Tel 0151-47390216
Fax 06347-8172094

```html
<!DOCTYPE html>
<html lang="de">
<head>
<meta charset="utf-8">
<title>Timo Harlang – Visitenkarten</title>
<link rel="stylesheet" href="https://fonts.googleapis.com/css2?family=Exo+2:wght@300;400;500;600&display=swap">
<style>
  :root {
    --page: #ffffff;
    --card: #000000;
    --silver: #c9c9c9;
    --silver-light: #e6e6e6;
    --silver-dark: #8c8c8c;
    --text-light: #d8d8d8;
  }
  * { margin: 0; padding: 0; box-sizing: border-box; }
  html, body { width: 1200px; height: 900px; overflow: hidden; background: var(--page); }
  body { position: relative; font-family: "Exo 2", sans-serif; }

  .card {
    position: absolute;
    width: 454px;
    height: 280px;
    background: var(--card);
    border-radius: 8px;
    box-shadow: 2px 3px 5px rgba(0,0,0,0.35);
    overflow: hidden;
    color: var(--text-light);
  }
  .card--front-a { left: 102px; top: 116px; }
  .card--front-b { left: 646px; top: 116px; }
  .card--back-a  { left: 102px; top: 498px; }
  .card--back-b  { left: 646px; top: 498px; }

  .card__rule {
    position: absolute; left: 0; right: 0; height: 2px;
    background: linear-gradient(90deg, var(--silver-dark), var(--silver-light) 50%, var(--silver-dark));
  }
  .card--front-a .card__rule, .card--front-b .card__rule { top: 184px; }
  .card--back-a .card__rule, .card--back-b .card__rule { top: 189px; }

  .name {
    position: absolute;
    white-space: nowrap;
    color: var(--silver);
    letter-spacing: 0.3px;
    line-height: 1;
  }
  .name__first { font-weight: 500; }
  .name__last { font-weight: 300; }
  .name .sc { font-size: 0.78em; }

  .card--front-a .name, .card--front-b .name {
    left: 0; right: 0; top: 214px; text-align: center; font-size: 42px;
  }
  .card--back-a .name { left: 40px; top: 48px; font-size: 42px; }
  .card--back-b .name { left: 299px; top: 151px; font-size: 21px; }

  .mark {
    position: absolute;
    display: flex; align-items: center; gap: 10px;
    color: var(--silver); font-weight: 400; white-space: nowrap;
  }
  .mark__square { background: var(--silver); flex: none; }
  .card--front-a .mark { left: 0; right: 0; top: 58px; justify-content: center; font-size: 22px; }
  .card--front-a .mark__square { width: 60px; height: 60px; }
  .card--front-b .mark { left: 0; right: 0; top: 70px; justify-content: center; font-size: 22px; }
  .card--front-b .mark__square { width: 36px; height: 36px; }
  .card--back-a .mark { left: 330px; top: 20px; flex-direction: column; gap: 8px; font-size: 15px; }
  .card--back-a .mark__square { width: 104px; height: 104px; }
  .card--back-b .mark { left: 323px; top: 36px; flex-direction: column; gap: 6px; font-size: 15px; }
  .card--back-b .mark__square { width: 52px; height: 52px; }

  .address, .contact {
    position: absolute; left: 40px; font-weight: 400; font-style: normal; color: var(--text-light);
  }
  .address { top: 136px; font-size: 16px; line-height: 22px; }
  .contact { top: 201px; font-size: 13px; line-height: 17px; }
  .contact__mail { margin-bottom: 9px; }
</style>
</head>
<body>

  <section class="card card--front-a" aria-label="Vorderseite, Variante A">
    <div class="mark"><span class="mark__square"></span><span>Timo Harlang</span></div>
    <div class="card__rule"></div>
    <p class="name"><span class="name__first">T<span class="sc">IMO</span></span> <span class="name__last">H<span class="sc">ARLANG</span></span></p>
  </section>

  <section class="card card--front-b" aria-label="Vorderseite, Variante B">
    <div class="mark"><span class="mark__square"></span><span>Timo Harlang</span></div>
    <div class="card__rule"></div>
    <p class="name"><span class="name__first">T<span class="sc">IMO</span></span> <span class="name__last">H<span class="sc">ARLANG</span></span></p>
  </section>

  <section class="card card--back-a" aria-label="Rückseite, Variante A">
    <p class="name"><span class="name__first">T<span class="sc">IMO</span></span> <span class="name__last">H<span class="sc">ARLANG</span></span></p>
    <div class="mark"><span class="mark__square"></span><span>Timo Harlang</span></div>
    <address class="address">Lindenweg 17<br>67382 Wiesenau</address>
    <div class="card__rule"></div>
    <div class="contact">
      <p class="contact__mail">email: info@timo-harlang.de</p>
      <p>Tel 0151-47390216</p>
      <p>Fax 06347-8172094</p>
    </div>
  </section>

  <section class="card card--back-b" aria-label="Rückseite, Variante B">
    <div class="mark"><span class="mark__square"></span><span>Timo Harlang</span></div>
    <p class="name"><span class="name__first">T<span class="sc">IMO</span></span> <span class="name__last">H<span class="sc">ARLANG</span></span></p>
    <address class="address">Lindenweg 17<br>67382 Wiesenau</address>
    <div class="card__rule"></div>
    <div class="contact">
      <p class="contact__mail">email: info@timo-harlang.de</p>
      <p>Tel 0151-47390216</p>
      <p>Fax 06347-8172094</p>
    </div>
  </section>

</body>
</html>
```